Computer Training in the Education sector - Letterhead

We need a new letter head to be designed for the company. We provide computer training fro the Education Sector, both primary and private tertiary providers. The colours will need to tie in with the website www.lanternpathlearning.co.nz.
The company name is Lantern Path Co with the tag line of Computer Training for Educators.
The footer will need to have the following detail...
0508 KEY MENTOR
027 813 459
www.lanternpathlearning.co.nz / lessons@lanternpathlearning.co.nz
Updates

Thanks for the designs so far.

Some have watermarks in the background. Please don't worry about using watermarks as I will not be using a watermark in in a final design.
Regards,
Morris

Thank you for all the designs and the effort. There was some great concepts that came through.

Cheers
Morris

Industry/Entity Type

Computer

```html
<!DOCTYPE html>
<html lang="en">
<head>
<meta charset="utf-8">
<title>Lantern Path Co – Letterhead</title>
<link rel="stylesheet" href="https://fonts.googleapis.com/css2?family=Arimo:wght@400&family=Questrial&display=swap">
<style>
  :root {
    --backdrop: #b3b3b3;
    --paper: #ffffff;
    --ink: #1a1a1a;
    --brand-blue: #1f63b8;
    --footer-green: #8db52a;
    --footer-blue: #0b74c4;
    --footer-blue-deep: #1e4f97;
    --signature-tone: #e6e6e6;
  }
  * { box-sizing: border-box; margin: 0; padding: 0; }
  html, body { width: 1200px; height: 848px; overflow: hidden; }
  body {
    background: var(--backdrop);
    font-family: "Arimo", Arial, sans-serif;
    color: var(--ink);
    position: relative;
  }
  .letterhead {
    position: absolute;
    left: 331px; top: 42px;
    width: 540px; height: 764px;
    background: var(--paper);
    box-shadow: 0 1px 4px rgba(0,0,0,.25);
    overflow: hidden;
  }
  .brand-name {
    position: absolute;
    left: 46px; top: 68px;
    width: 92px;
    font-family: "Questrial", Arial, sans-serif;
    font-size: 16px; line-height: 18px;
    color: var(--brand-blue);
  }
  .tagline {
    position: absolute;
    left: 147px; top: 70px;
    font-family: "Questrial", Arial, sans-serif;
    font-size: 13.5px; line-height: 15px;
    color: var(--brand-blue);
    letter-spacing: -0.2px;
  }
  .contact {
    position: absolute;
    right: 36px; top: 59px;
    text-align: right;
    font-style: normal;
    font-family: "Questrial", Arial, sans-serif;
    font-size: 7.5px; line-height: 10.6px;
    color: var(--ink);
  }
  .contact .label { margin-right: 8px; }
  .contact .web {
    display: block; margin-top: 16px;
    color: var(--brand-blue);
  }
  .letter-body {
    position: absolute;
    left: 46px; top: 178px;
    width: 320px;
    font-size: 7.7px; line-height: 10.9px;
    text-align: justify;
    color: var(--ink);
  }
  .letter-body p { margin-bottom: 10.9px; }
  .signature {
    position: absolute;
    left: 39px; top: 516px;
    width: 146px; height: 42px;
    background: var(--signature-tone);
  }
  .footer-band {
    position: absolute;
    left: 0; bottom: 0;
    width: 540px; height: 78px;
    background: linear-gradient(90deg, var(--footer-green) 0%, var(--footer-blue) 45%, var(--footer-blue-deep) 100%);
  }
</style>
</head>
<body>
  <main class="letterhead">
    <header>
      <div class="brand-name">Lantern Path Co</div>
      <div class="tagline">Computer Training<br>for Educators</div>
      <address class="contact">
        0508 KEY MENTOR<br>
        <span class="label">p.</span>027 813 459<br>
        <span class="label">m.</span>lessons@lanternpathlearning.co.nz
        <span class="web">www.lanternpathlearning.co.nz</span>
      </address>
    </header>

    <section class="letter-body">
      <p>Lorem ipsum dolor sit amet, consectetur adipiscing elit. Suspendisse blandit, nulla ut porta scelerisque, urna massa ultrices ligula, at rutrum nunc ipsum ac risus. Sed consectetur nulla non velit sollicitudin a eleifend tortor pellentesque. Cras laoreet iaculis pretium. Vestibulum vitae sapien at metus fermentum tempus quis sed mauris. Donec blandit metus in nibh laoreet ultrices. Nullam molestie, turpis ac adipiscing tincidunt, urna justo eleifend ligula, et consectetur massa lorem ac risus. Aenean quis justo vitae massa accumsan ultricies posuere eget diam. Aenean ipsum sapien, pellentesque id semper vitae, mattis eget enim. Vestibulum congue tincidunt enim ut tristique. Praesent interdum malesuada adipiscing. Donec quis felis massa.</p>
      <p>Praesent nisl libero, pretium eu interdum eu, rhoncus ut lorem. Praesent faucibus lorem sit amet ligula consequat adipiscing. Morbi adipiscing dapibus erat, eu condimentum nibh vestibulum vel. In elementum nulla id arcu bibendum malesuada. Donec non nulla sit amet tortor volutpat placerat id vel felis. Maecenas accumsan, augue ac molestie iaculis, justo risus vestibulum dolor, eu ullamcorper nulla orci ac est. Donec tristique sem a nisl euismod convallis id ac lacus. Sed pretium bibendum velit eget mollis. Praesent porta suscipit lacus, ac porta odio faucibus eu. Donec accumsan laoreet nisl et hendrerit. In fringilla enim ac urna sagittis convallis.</p>
      <p>Nullam est mi, euismod ac pretium ac, consequat eu urna. Aliquam egestas, elit non gravida pellentesque, purus orci facilisis est, vitae ultricies turpis nisl non justo. Fusce varius libero nec nibh elementum consequat ut sed elit. Integer lorem erat, varius ac malesuada vitae, convallis sit amet libero. Cras sagittis, urna eu scelerisque auctor, elit tellus vestibulum mi, non elementum metus eros ut dolor. Etiam porta est dolor. Vivamus suscipit lobortis commodo. Integer convallis, nunc tincidunt rhoncus lobortis, sapien purus ultrices orci, quis dignissim urna felis dictum elit.</p>
    </section>

    <div class="signature" role="img" aria-label="Handwritten signature of the sender"></div>

    <div class="footer-band" role="img" aria-label="Decorative footer band in the brand's green and blue tones"></div>
  </main>
</body>
</html>
```